Pre-Listing Template, This is intended to explain the selling process and make sellers comfortable

I'm looking for a branded template that I can mail to home sellers before I meet with them to discuss selling their home. I work at LU/PEX and would want their logos as part of the template. I've included a photo of the bottom of a page that I think looks good. I would like for you to put my information in a similar fashion. The colors should be Red, White, and Blue. I would also like it to follow the attached general outline.
Cover page: I would like the cover page to have a photo box for the client's home and the title "Pre-Listing Report"
Table of Contents:
Page 1 Mission statement
Please state "Mission Statement" and then provide a box for me to place the text
Page 2 Agent Profile
Please use my photo that I have provided and give me a box that I can place my text
Page 3 About LU/PEX
Use a photo or some type of graphic with a text box
Page 4 Testimonials
The text boxes per page for testimonials
Page 5 Testimonials
Page 6 Marketing Plan
Bold type with text box below. Each page should have this
Page 7 Marketing Plan
Page 8 Marketing Plan
Page 9 Online Exposure
I've included an example in the photo section of this brief
Page 10 Print Advertising
Should have newspaper, just listed post card, brochure, Porch & Gable St. Augustine edition.
Page 11 Questions You Should Ask your Realtor
I've included a photo of a similar one. Please omit question 14
Page 12 Seller's Homework
Photo with text box below
Target Market(s)
Residents of NE Florida with a home to sell
Industry/Entity Type
Real Estate Agent
Requirements
Must have
- Thank you so much for taking the time to review my project! This is my first time on pixel tavern so if you need anything don't hesitate to ask.
- I will need lightly shaded boxes for me to list information or suggested places for pictures/graphics once you are done with the template
Nice to have
- I would like a date in the top right corner of the title page, LU/PEX Logo on every page consistently throughout the presentation.

```html
<!DOCTYPE html>
<html lang="en">
<head>
<meta charset="utf-8">
<title>Pre-Listing Package</title>
<link href="https://fonts.googleapis.com/css2?family=Open+Sans:ital,wght@0,400;0,700;1,400&display=swap" rel="stylesheet">
<style>
  :root {
    --brand-red: #d1232b;
    --brand-navy: #24408e;
    --sky-tint: #e0f2fc;
    --ink: #111111;
    --date-blue: #1f3a8a;
    --rule-grey: #9a9a9a;
    --paper: #ffffff;
    --agent-green: #5f8a4a;
  }
  * { box-sizing: border-box; margin: 0; padding: 0; }
  html, body { width: 927px; height: 1200px; overflow: hidden; background: var(--paper); }
  body { font-family: "Open Sans", "Calibri", sans-serif; position: relative; }
  .cover-date {
    position: absolute; right: 53px; top: 47px;
    color: var(--date-blue); font-size: 21px;
  }
  .title-band {
    position: absolute; left: 51px; top: 228px; width: 825px; height: 99px;
    background: var(--brand-red); display: flex; align-items: center; justify-content: center;
  }
  .title-band h1 { color: var(--paper); font-size: 46px; font-weight: 700; letter-spacing: -0.5px; }
  .home-photo-box {
    position: absolute; left: 51px; top: 327px; width: 825px; height: 474px;
    background: var(--sky-tint); display: flex; align-items: center; justify-content: center;
  }
  .home-photo-box span { font-style: italic; font-size: 21px; color: var(--ink); }
  .agent-band {
    position: absolute; left: 51px; top: 801px; width: 825px; height: 348px;
    background: var(--brand-navy);
  }
  .agent-photo {
    position: absolute; left: 24px; top: 48px; width: 172px; height: 180px;
    background: linear-gradient(180deg, var(--agent-green) 0%, #7fa064 45%, #c9d3e2 100%);
  }
  .prepared-card {
    position: absolute; left: 216px; top: 48px; width: 584px; height: 180px;
    background: var(--paper); padding: 30px 32px 0 30px;
  }
  .prepared-card p { font-style: italic; font-size: 17px; color: var(--ink); }
  .prepared-card .line { height: 1px; background: var(--rule-grey); margin-top: 35px; }
  .prepared-card .line + .line { margin-top: 52px; }
</style>
</head>
<body>
  <div class="cover-date">January 28, 2018</div>
  <header class="title-band"><h1>Pre-Listing Package</h1></header>
  <section class="home-photo-box" role="img" aria-label="Placeholder for a photo of the client's home">
    <span>Photo placement box</span>
  </section>
  <section class="agent-band">
    <div class="agent-photo" role="img" aria-label="Portrait photo of the listing agent"></div>
    <div class="prepared-card">
      <p>Prepared for:</p>
      <div class="line"></div>
      <div class="line"></div>
    </div>
  </section>
</body>
</html>
```